seeking a modern Business Card design for Roof Plumbering Business

wexcombe roof plumbing is a local metal re-roof and new construction specialist. We are seeking a modern business card to assist with networking within the industry. Our services are predominantly the installation of metal roofs on new houses, however we also do re-roofs when an existing roof needs replacing. We service both residential and commercial properties. Please include the below details on the card:
Name: Owen Wexcombe
Phone: 0471 385 962
Email: owenwexcomberoofing@mailnest.example

Residential & Commercial
Re-roof & New Construction
Fully Insured

I have uploaded our business logo, which we think would suit a black background. Please use all lower case for business name.
Cheers
Updates

Hey Guys, As requested I've uploaded a Pdf version of my logo. Hopefully this help. Thanks

Industry/Entity Type

Business

Contact Information for Business Card

Name: Owen Wexcombe
Phone: 0471 385 962

Residential & Commercial
Fully Insured

Font styles to use
Serif
Sans Serif

Requirements
Must have
• Name must be all lower case "wexcombe roof plumbing"
Nice to have
• Stick with Logo Colours

```html
<!DOCTYPE html>
<html lang="en">
<head>
<meta charset="utf-8">
<title>wexcombe roof plumbing — business card</title>
<link href="https://fonts.googleapis.com/css2?family=Montserrat:wght@400;500;700&display=swap" rel="stylesheet">
<style>
  :root {
    --backdrop: #939393;
    --card: #1f1f1f;
    --brand-blue: #37a0d4;
    --ink-light: #ffffff;
    --ink-dark: #1b2229;
  }
  html, body {
    margin: 0;
    width: 1200px;
    height: 1200px;
    overflow: hidden;
    background: var(--backdrop);
    font-family: "Montserrat", sans-serif;
  }
  .card {
    position: absolute;
    left: 175px;
    top: 363px;
    width: 850px;
    height: 473px;
    background: var(--card);
    overflow: hidden;
  }
  .brand {
    position: absolute;
    left: 462px;
    top: 120px;
    width: 270px;
    color: var(--brand-blue);
    font-weight: 400;
    text-align: left;
    line-height: 1;
  }
  .brand-name {
    display: block;
    font-size: 50px;
    letter-spacing: 0.5px;
  }
  .brand-trade {
    display: block;
    margin-top: 8px;
    font-size: 23px;
    letter-spacing: 6.5px;
  }
  .contact {
    position: absolute;
    left: 81px;
    top: 265px;
    color: var(--ink-light);
  }
  .contact-name {
    margin: 0 0 10px;
    font-size: 24px;
    font-weight: 700;
  }
  .contact-line {
    display: flex;
    align-items: center;
    height: 27px;
    font-size: 18px;
    font-weight: 400;
  }
  .contact-line svg {
    width: 19px;
    height: 16px;
    margin-right: 18px;
    flex: none;
  }
  .services-band {
    position: absolute;
    left: 0;
    top: 395px;
    width: 100%;
    height: 55px;
    background: var(--brand-blue);
    color: var(--ink-dark);
    font-size: 18px;
    font-weight: 500;
  }
  .service, .divider {
    position: absolute;
    top: 16px;
    white-space: nowrap;
  }
</style>
</head>
<body>
  <div class="card">
    <div class="brand">
      <span class="brand-name">wexcombe</span>
      <span class="brand-trade">roof plumbing</span>
    </div>

    <div class="contact">
      <p class="contact-name">Owen Wexcombe</p>
      <div class="contact-line">
        <svg viewBox="0 0 20 16" aria-hidden="true">
          <path d="M1 5 C4 1 16 1 19 5 L16 7 L14 4 H6 L4 7 Z" fill="var(--brand-blue)"/>
          <path d="M6 6 H14 L17 14 H3 Z" fill="none" stroke="var(--brand-blue)" stroke-width="2"/>
          <circle cx="10" cy="10.5" r="2" fill="var(--brand-blue)"/>
        </svg>
        <span>0471 385 962</span>
      </div>
      <div class="contact-line">
        <svg viewBox="0 0 20 16" aria-hidden="true">
          <rect x="1" y="2" width="18" height="12" fill="none" stroke="var(--brand-blue)" stroke-width="2"/>
          <path d="M1 2 L10 9 L19 2 M1 14 L8 8 M19 14 L12 8" fill="none" stroke="var(--brand-blue)" stroke-width="1.8"/>
        </svg>
        <span>owenwexcomberoofing@mailnest.example</span>
      </div>
    </div>

    <div class="services-band">
      <span class="service" style="left:81px">Residential &amp; Commercial</span>
      <span class="divider" style="left:328px">-</span>
      <span class="service" style="left:354px">Re-roof &amp; New Construction</span>
      <span class="divider" style="left:630px">-</span>
      <span class="service" style="left:657px">Fully Insured</span>
    </div>
  </div>
</body>
</html>
```